bluefernworks.com website design

We're looking for a website design for Bluefernworks.com .
Bluefern is a manufacturer of high visibility traffic safety equipment and gear.. Our initial site will be a product catalog site featuring traffic cones . We will eventually expand to include traffic barriers, mesh signs, safety clothing and more. Our logo and product pictures can be found at bluefernworks.com .
Updates

Target Market(s)

We service a wide range of customers with our focus markets being construction, manufacturing and municipalities.

Industry/Entity Type

Safety Products

Number of Pages Required

1 page

Font styles to use
Sans Serif

Requirements
Must have
• company logo w/compatible color scheme

```html
<!DOCTYPE html>
<html lang="en">
<head>
<meta charset="UTF-8">
<title>Bluefern Safety Products</title>
<link rel="stylesheet" href="https://fonts.googleapis.com/css2?family=Montserrat:wght@600;700&family=Roboto:wght@400;500&display=swap">
<style>
:root{
  --orange:#e8913d;
  --orange-dark:#d97f2a;
  --green:#7cba6a;
  --green-dark:#5e9f4d;
  --cream:#fdf8f0;
  --ink:#222;
  --text:#333;
  --night:#121212;
  --white:#fff;
}
*{margin:0;padding:0;box-sizing:border-box}
html,body{width:1200px;height:3661px;overflow:hidden}
body{position:relative;background:var(--white);font-family:'Roboto',sans-serif;color:var(--text)}
.abs{position:absolute}
.heading{font-family:'Montserrat',sans-serif;font-weight:700;color:var(--orange);font-size:52px;line-height:1}
.btn{position:absolute;display:flex;align-items:center;justify-content:center;background:var(--green);color:var(--white);font-family:'Roboto',sans-serif;font-weight:500;border-radius:30px;box-shadow:0 2px 0 var(--green-dark)}
.brand{font-family:'Montserrat',sans-serif;font-weight:700;color:var(--orange);display:flex;align-items:center;gap:12px}
.brand-dot{width:40px;height:40px;border-radius:50%;background:var(--orange)}

/* header */
.site-header{top:0;left:0;width:1200px;height:110px;background:var(--white)}
.catalog-btn{left:149px;top:18px;width:229px;height:33px;font-size:13px;border-radius:8px;box-shadow:none}
.nav-link{position:absolute;top:72px;font-size:16px;color:#555}
.nav-link.active{color:var(--orange);font-weight:500}
.header-brand{left:478px;top:28px;font-size:34px}
.header-mail{left:853px;top:18px;display:flex;align-items:center;gap:8px;font-size:13px;color:#333}
.mail-icon{width:30px;height:30px;border-radius:50%;background:var(--orange);display:flex;align-items:center;justify-content:center}

/* hero */
.hero{top:110px;left:0;width:1200px;height:672px}
.hero-photo{position:absolute;inset:0;background:linear-gradient(135deg,#5a4236 0%,#6b6a68 35%,#7a7a73 55%,#b49b3e 75%,#6b5d50 100%)}
.hero-title{position:absolute;top:210px;left:0;width:1200px;text-align:center;font-family:'Montserrat',sans-serif;font-weight:700;font-size:66px;line-height:78px;color:var(--white);text-shadow:0 2px 8px rgba(0,0,0,.45)}
.hero-btn{left:499px;top:390px;width:201px;height:55px;font-family:'Montserrat',sans-serif;font-weight:600;font-size:21px}

/* products */
.products-title{top:897px;left:0;width:1200px;text-align:center}
.intro{top:974px;left:0;width:1200px;text-align:center;font-family:'Montserrat',sans-serif;font-size:12.5px;line-height:21px;color:#222}
.product{position:absolute;width:210px}
.product-photo{width:210px;height:193px;border-radius:12px}
.product-name{margin-top:14px;text-align:center;font-family:'Montserrat',sans-serif;font-weight:600;font-size:20px;color:var(--orange)}
.view-btn{left:481px;top:1593px;width:239px;height:48px;font-size:19px}

/* about */
.about{top:1720px;left:0;width:1200px;height:540px}
.about-mark{left:196px;top:1863px;width:256px;height:256px;border-radius:50%;background:var(--orange);display:flex;align-items:center;justify-content:center;font-family:'Montserrat',sans-serif;font-weight:700;font-size:40px;color:var(--white)}
.about-title{top:1818px;left:559px}
.about-text{top:1902px;left:559px;width:500px;font-family:'Montserrat',sans-serif;font-size:12.3px;line-height:17.4px;color:#333}
.about-btn{left:559px;top:2070px;width:266px;height:47px;font-size:19px}

/* why */
.why{top:2236px;left:0;width:1200px;height:700px;background:linear-gradient(180deg,#fff 0%,#f2f2f2 50%,#fafafa 100%)}
.why-title{top:2388px;left:149px}
.why-list{top:2450px;left:149px;list-style:none}
.why-list li{display:flex;align-items:center;gap:8px;height:35px;font-size:18px;color:#333}
.why-photo{left:627px;top:2386px;width:424px;height:424px;border-radius:50%;border:6px solid var(--orange);background:linear-gradient(160deg,#c9c7c0 0%,#9a968c 40%,#6e6c68 70%,#d24b32 100%)}

/* contact */
.contact{left:151px;top:2939px;width:898px;height:402px;border-radius:20px;background:var(--orange);z-index:3}
.contact-title{position:absolute;top:50px;left:0;width:898px;text-align:center;color:var(--white)}
.field{position:absolute;border:1px solid rgba(255,255,255,.85);color:var(--white);font-size:12.5px;padding:9px 13px}
.submit-btn{left:388px;top:286px;width:122px;height:49px;font-size:18px;border:2px solid var(--white)}

/* footer */
.footer{top:3220px;left:0;width:1200px;height:441px;z-index:2}
.footer-mail{left:173px;top:3417px;display:flex;align-items:center;gap:8px;font-size:15px;color:var(--white);z-index:4}
.footer-brand{left:470px;top:3405px;font-size:36px;z-index:4}
.social{position:absolute;top:3404px;width:34px;height:34px;border-radius:50%;border:2px solid var(--white);z-index:4}
.footer-rule{left:28px;top:3505px;width:1144px;height:1px;background:rgba(255,255,255,.25);z-index:4}
.footer-nav{position:absolute;top:3546px;font-size:16px;color:var(--white);z-index:4}
.copyright{top:3600px;left:0;width:1200px;text-align:center;font-size:12px;color:var(--white);z-index:4}
</style>
</head>
<body>

<header class="abs site-header">
  <div class="btn catalog-btn">DOWNLOAD PRODUCT CATALOG</div>
  <span class="nav-link active" style="left:149px">Home</span>
  <span class="nav-link" style="left:224px">About Us</span>
  <span class="nav-link" style="left:322px">Services</span>
  <div class="abs brand header-brand"><span class="brand-dot"></span>Bluefern</div>
  <div class="abs header-mail">
    <span class="mail-icon"><svg width="14" height="10" viewBox="0 0 14 10"><rect x="0.5" y="0.5" width="13" height="9" rx="1" fill="none" stroke="#fff"/><path d="M1 1l6 5 6-5" fill="none" stroke="#fff"/></svg></span>
    info@bluefernworks.com
  </div>
  <span class="nav-link" style="left:842px">Traffic Cones</span>
  <span class="nav-link" style="left:971px">Contact Us</span>
</header>

<section class="abs hero">
  <div class="hero-photo" role="img" aria-label="Safety gear on a table: work boots, hard hat, goggles, gloves and ear defenders"></div>
  <svg class="abs" style="left:0;top:0" width="1200" height="672" viewBox="0 0 1200 672">
    <path d="M0 525 Q560 770 1200 485 L1200 672 L0 672 Z" fill="#fff"/>
    <path d="M0 530 Q520 790 1080 570" fill="none" stroke="#e8913d" stroke-width="9"/>
  </svg>
  <h1 class="hero-title">We Prioritise Your<br>Safety</h1>
  <div class="btn hero-btn">GET IN TOUCH</div>
</section>

<h2 class="abs heading products-title">Our Products</h2>
<p class="abs intro">Lorem ipsum dolor sit amet, consectetur adipiscing elit, sed do eiusmod tempor incididunt ut labore et dolore magna aliqua.<br>Ut enim ad minim veniam, quis nostrud exercitation ullamco laboris nisi ut aliquip ex ea commodo consequat.</p>

<div class="product" style="left:149px;top:1051px"><div class="product-photo" role="img" aria-label="Row of traffic cones on a road" style="background:linear-gradient(160deg,#b9bcc0,#5c5e62 60%,#e2621f)"></div><div class="product-name">Traffic Cones</div></div>
<div class="product" style="left:380px;top:1051px"><div class="product-photo" role="img" aria-label="Striped traffic barriers on a street" style="background:linear-gradient(160deg,#8a8f86,#b7b4ab 50%,#e8782e)"></div><div class="product-name">Traffic Barriers</div></div>
<div class="product" style="left:610px;top:1051px"><div class="product-photo" role="img" aria-label="Mesh fence with a stop sign" style="background:linear-gradient(160deg,#c5cacd,#7c7a70 60%,#a8402f)"></div><div class="product-name">Mesh Sign</div></div>
<div class="product" style="left:839px;top:1051px"><div class="product-photo" role="img" aria-label="Safety clothing and gear on wooden boards" style="background:linear-gradient(160deg,#6a5540,#caa35e 50%,#e5c53a)"></div><div class="product-name">Safety Clothing</div></div>

<div class="product" style="left:149px;top:1318px"><div class="product-photo" role="img" aria-label="Orange hard hat with tools" style="background:linear-gradient(160deg,#9a9690,#e8622a 50%,#8e8a84)"></div><div class="product-name">Safety Hat</div></div>
<div class="product" style="left:380px;top:1318px"><div class="product-photo" role="img" aria-label="Worker wearing safety glasses and helmet" style="background:linear-gradient(160deg,#5b7fa3,#c8b9a6 50%,#d85b2a)"></div><div class="product-name">Safety Specs</div></div>
<div class="product" style="left:610px;top:1318px"><div class="product-photo" role="img" aria-label="Worker in safety gloves laying stones" style="background:linear-gradient(160deg,#e48a30,#8d8578 50%,#c9c4bb)"></div><div class="product-name">Safety Gloves</div></div>
<div class="product" style="left:839px;top:1318px"><div class="product-photo" role="img" aria-label="Black gear case with red stripe" style="background:linear-gradient(160deg,#dfe3e8,#2b2b2e 50%,#c8282a)"></div><div class="product-name">Safety Gear</div></div>

<div class="btn view-btn">VIEW ALL PRODUCTS</div>

<svg class="abs about" width="1200" height="540" viewBox="0 0 1200 540">
  <path d="M0 0 H1200 V432 Q600 560 0 432 Z" fill="#fdf8f0"/>
  <path d="M0 434 Q600 560 1200 434" fill="none" stroke="#e8913d" stroke-width="9"/>
</svg>
<div class="abs about-mark">Bluefern</div>
<h2 class="abs heading about-title">About Bluefern</h2>
<p class="abs about-text">Lorem ipsum dolor sit amet, consectetur adipiscing elit, sed do eiusmod tempor incididunt ut labore et dolore magna aliqua. Ut enim ad minim veniam, quis nostrud exercitation ullamco laboris nisi ut aliquip ex ea commodo consequat. Duis aute irure dolor in reprehenderit in voluptate velit esse cillum dolore eu fugiat nulla pariatur. Excepteur sint occaecat cupidatat non proident, sunt in culpa qui officia deserunt mollit anim id est laborum.Sed ut perspiciatis unde omnis iste natus error sit voluptatem accusantium doloremque laudantium, totam rem aperiam, eaque ipsa quae atecto beatae vitae dicta sunt explicabo.</p>
<div class="btn about-btn">LEARN MORE ABOUT US</div>

<section class="abs why"></section>
<h2 class="abs heading why-title">Why Choose Us</h2>
<ul class="abs why-list">
  <li><svg width="20" height="12" viewBox="0 0 20 12"><path d="M0 3h5v9H0z M6 4l4-4h2l-1 4h8v3h-6v2h5v3H6z" fill="#7cba6a"/></svg>Integer scelerisque neque eu varius aliquam.</li>
  <li><svg width="20" height="12" viewBox="0 0 20 12"><path d="M0 3h5v9H0z M6 4l4-4h2l-1 4h8v3h-6v2h5v3H6z" fill="#7cba6a"/></svg>Cras ut tortor eu ante mattis blandit ac a odio.</li>
  <li><svg width="20" height="12" viewBox="0 0 20 12"><path d="M0 3h5v9H0z M6 4l4-4h2l-1 4h8v3h-6v2h5v3H6z" fill="#7cba6a"/></svg>Aenean hendrerit libero sit amet et molestie.</li>
  <li><svg width="20" height="12" viewBox="0 0 20 12"><path d="M0 3h5v9H0z M6 4l4-4h2l-1 4h8v3h-6v2h5v3H6z" fill="#7cba6a"/></svg>Phasellus efficitut luctus pellentesque.</li>
  <li><svg width="20" height="12" viewBox="0 0 20 12"><path d="M0 3h5v9H0z M6 4l4-4h2l-1 4h8v3h-6v2h5v3H6z" fill="#7cba6a"/></svg>Donec tr velit elementum lobortis finibus.</li>
  <li><svg width="20" height="12" viewBox="0 0 20 12"><path d="M0 3h5v9H0z M6 4l4-4h2l-1 4h8v3h-6v2h5v3H6z" fill="#7cba6a"/></svg>Sed interdum ante ut turpis interdum mollis.</li>
  <li><svg width="20" height="12" viewBox="0 0 20 12"><path d="M0 3h5v9H0z M6 4l4-4h2l-1 4h8v3h-6v2h5v3H6z" fill="#7cba6a"/></svg>Cras a dolor nec odio scelerisque gravida.</li>
  <li><svg width="20" height="12" viewBox="0 0 20 12"><path d="M0 3h5v9H0z M6 4l4-4h2l-1 4h8v3h-6v2h5v3H6z" fill="#7cba6a"/></svg>Aliquam feugiat augue rpis auctor laoreet.</li>
</ul>
<div class="abs why-photo" role="img" aria-label="Traffic cones lined along a road with a yellow line"></div>

<section class="abs contact">
  <h2 class="heading contact-title">Contact Us</h2>
  <div class="field" style="left:109px;top:139px;width:218px;height:37px">Name</div>
  <div class="field" style="left:339px;top:139px;width:218px;height:37px">Email Address</div>
  <div class="field" style="left:570px;top:139px;width:219px;height:37px">Phone Number</div>
  <div class="field" style="left:109px;top:195px;width:680px;height:116px">Message</div>
  <div class="btn submit-btn">SUBMIT</div>
</section>

<footer class="abs footer">
  <svg class="abs" style="left:0;top:0" width="1200" height="441" viewBox="0 0 1200 441">
    <defs>
      <linearGradient id="footerShade" x1="0" y1="0" x2="1" y2="1">
        <stop offset="0" stop-color="#1b1a18"/>
        <stop offset="0.5" stop-color="#0e0e0e"/>
        <stop offset="1" stop-color="#2a1c12"/>
      </linearGradient>
    </defs>
    <path d="M0 140 Q620 20 1200 130 L1200 441 L0 441 Z" fill="url(#footerShade)" role="img" aria-label="Dark night street with traffic cones"/>
    <path d="M1050 70 Q1130 85 1200 115" fill="none" stroke="#e8913d" stroke-width="9"/>
  </svg>
</footer>
<div class="abs footer-mail">
  <span class="mail-icon"><svg width="14" height="10" viewBox="0 0 14 10"><rect x="0.5" y="0.5" width="13" height="9" rx="1" fill="none" stroke="#fff"/><path d="M1 1l6 5 6-5" fill="none" stroke="#fff"/></svg></span>
  info@bluefernworks.com
</div>
<div class="abs brand footer-brand"><span class="brand-dot"></span>Bluefern</div>
<span class="social" style="left:974px"></span>
<span class="social" style="left:1017px"></span>
<div class="abs footer-rule"></div>
<span class="footer-nav" style="left:338px">Home</span>
<span class="footer-nav" style="left:426px">About Us</span>
<span class="footer-nav" style="left:537px">Services</span>
<span class="footer-nav" style="left:642px">Traffic Cones</span>
<span class="footer-nav" style="left:783px">Contact us</span>
<p class="abs copyright">Copyrights ©2023 Bluefern Safety Products. All Rights Reserved</p>

</body>
</html>
```